Letterhead design - Harwick Group

We have just had our Logo created and our now wantng a letterhead design to incorporate this. Please use the same colours as in the logo, which is attached.
Please use the company details below
P O Box 86, Bleneheim 7315
Ph: 03 642 1937
dave@harwickgroup.co.nz
We would like a professional look
We need an overall letterhead design for our varied group of buisinesses which are based in NZ and overseas. We grow and develop buisinesses. Our companies began in NZ but we now have branches overseas as well. People are our greatest asset and we employ some incredible staff. Our buisinesses are scientific, innovative and growing in size and expertise with a financial base.

Target Market(s)

Professionals

Industry/Entity Type

Investment

Requirements
Must have
• Easy to read.
• Please use the same colours as in the logo
• Please use the company details below
• P O Box 86, Bleneheim 7315
• Ph: 03 642 1937
• dave@harwickgroup.co.nz

```html
<!DOCTYPE html>
<html lang="en">
<head>
<meta charset="utf-8">
<title>Harwick Group Letterhead</title>
<link href="https://fonts.googleapis.com/css2?family=Lato:wght@400;700;900&family=Roboto:wght@400&display=swap" rel="stylesheet">
<style>
  :root {
    --brand-green: #1fb574;
    --brand-grey: #666666;
    --backdrop: #cbcbcb;
    --paper: #ffffff;
    --ink: #3f3f3f;
    --ink-soft: #555555;
  }
  * { margin: 0; padding: 0; box-sizing: border-box; }
  html, body { width: 1200px; height: 1200px; overflow: hidden; background: var(--backdrop); }
  .letterhead {
    position: absolute; left: 226px; top: 71px; width: 748px; height: 1059px;
    background: var(--paper); font-family: "Lato", sans-serif; color: var(--ink);
  }
  .brand {
    position: absolute; left: 48px; top: 86px; display: flex; align-items: center; gap: 10px;
  }
  .brand-mark { width: 46px; height: 46px; background: var(--brand-green); }
  .brand-name {
    font-family: "Lato", sans-serif; font-weight: 900; font-size: 30px;
    letter-spacing: 0.5px; color: var(--brand-green); text-transform: uppercase;
  }
  .contact {
    position: absolute; left: 518px; top: 80px; list-style: none;
    font-family: "Roboto", sans-serif; font-size: 13px; color: #222;
  }
  .contact li { display: flex; align-items: center; gap: 6px; height: 21.5px; }
  .contact svg { width: 13px; height: 13px; flex: none; }
  .recipient { position: absolute; left: 50px; top: 259px; }
  .recipient-name { font-weight: 700; font-size: 13px; color: #333; letter-spacing: -0.1px; }
  .recipient-role { font-size: 9.5px; color: var(--ink-soft); margin-top: 1px; }
  .letter-date { margin-top: 8px; margin-left: -3px; font-size: 9.5px; color: #333; }
  .letter-date strong { font-size: 12px; font-weight: 700; }
  .letter-date sup { font-size: 5px; }
  .letter-body {
    position: absolute; left: 50px; top: 364px; width: 652px;
    font-size: 11.2px; line-height: 17.6px; color: var(--ink-soft);
  }
  .letter-body p { margin-bottom: 35.6px; }
  .letter-body p.closing-line { margin-top: -17.6px; }
  .sign-off { position: absolute; left: 49px; top: 791px; font-size: 12.5px; color: var(--ink-soft); }
  .signature {
    position: absolute; left: 50px; top: 816px; width: 176px; height: 28px;
    background: linear-gradient(90deg, #e9e9e9, #f3f3f3);
  }
  .footer-band { position: absolute; left: 0; bottom: 0; width: 748px; height: 26px; display: block; }
</style>
</head>
<body>
  <main class="letterhead">
    <header>
      <div class="brand">
        <span class="brand-mark"></span>
        <span class="brand-name">Harwick Group</span>
      </div>
      <ul class="contact">
        <li>
          <svg viewBox="0 0 16 16" aria-hidden="true"><path fill="var(--brand-green)" d="M3.6 1.5l2.3 2.4-1.3 1.8c.9 2 2.6 3.7 4.7 4.7l1.8-1.3 2.4 2.3-1.6 2.1C6.7 13.4 2.6 9.3 1.5 3.1z"/><path d="M9.5 2.2a4.5 4.5 0 0 1 4.3 4.3M9.3 4.4a2.3 2.3 0 0 1 2.3 2.3" stroke="var(--brand-green)" stroke-width="1.3" fill="none"/></svg>
          <span>03 642 1937</span>
        </li>
        <li>
          <svg viewBox="0 0 16 16" aria-hidden="true"><rect x="1" y="3" width="14" height="10" fill="var(--brand-green)"/><path d="M1.5 3.5L8 9l6.5-5.5" stroke="#fff" stroke-width="1.2" fill="none"/></svg>
          <span>P O Box 86, Bleneheim 7315</span>
        </li>
        <li>
          <svg viewBox="0 0 16 16" aria-hidden="true"><g stroke="var(--brand-green)" stroke-width="1.2" fill="none"><circle cx="8" cy="8" r="6.4"/><ellipse cx="8" cy="8" rx="2.8" ry="6.4"/><path d="M1.6 8h12.8M2.6 4.8h10.8M2.6 11.2h10.8"/></g></svg>
          <span>dave@harwickgroup.co.nz</span>
        </li>
      </ul>
    </header>

    <section class="recipient">
      <p class="recipient-name">RENWICK ALDER</p>
      <p class="recipient-role">Maneging Director</p>
      <p class="letter-date"><strong>Date:</strong> 11<sup>st</sup> February, 2018</p>
    </section>

    <section class="letter-body">
      <p>Lorem ipsum dolor sit amet, consectetur adipisicing elit, sed do eiusmod tempor incididunt ut labore et dolore magna sdfsd sfdsf sd veniam, quis nostrud exercitation&nbsp; ullamco laboris nisi ut aliquip ex ea commodo consequat. Duis aute irure dolor in repsdfsdf sdfsd ullamco laboris nisi ut aliquip ex ea commodo consequat. Duis aute irure dolor in reprehenderit in voluptate velit esse cillum dolore ullamco laboris nisi ut aliquip ex ea commodo consequat. Duis aute irure dolor in reprehenderit in voluptate velit esse cillum dolore ullamco laboris nisi ut aliquip ex ea commodo consequat.</p>
      <p>Lorem ipsum dolor sit amet, consectetur adipisicing elit, sed do eiusmod tempor incididunt ut labore et dolore magna sdfsdfsdfdfdf veniam, quis nostrud exercitation&nbsp; ullamco laboris nisi ut aliquip ex ea commodo consequat. Duis aute irure dolor in repdfgfgr rtetg. ullamco laboris nisi ut aliquip ex ea commodo consequat. Duis aute irure dolor in reprehenderit in voluptate velit esse cillum dolore ullamco laboris nisi ut aliquip ex ea commodo consequat. Duis aute irure dolor in reprehenderit in voluptate velit esse cillum dolore ullamco laboris nisi ut aliquip ex ea commodo consequat.</p>
      <p>Lorem ipsum dolor sit amet, consectetur adipisicing elit, sed do eiusmod tempor incididunt ut labore et dolore magna sds dff fefsdf veniam, quis nostrud exercitation&nbsp; ullamco laboris nisi ut aliquip ex ea commodo consequat. Duis aute irure dolor in repsdfsdf dfdsf ullamco laboris nisi ut aliquip ex ea commodo consequat. Duis aute irure dolor in reprehenderit in voluptate velit esse cillum dolore ullamco laboris nisi ut aliquip ex ea commodo consequat. Duis aute irure dolor in reprehenderit in voluptate velit esse cillum dolore ullamco laboris nisi ut aliquip ex ea commodo consequat.</p>
      <p class="closing-line">dolor sit amet, consectetur, adipisci velit, sed quia non numquam eius modi tempora incidunt ut labore et</p>
    </section>

    <p class="sign-off">Regards</p>
    <div class="signature" role="img" aria-label="Handwritten signature of the sender"></div>

    <svg class="footer-band" viewBox="0 0 748 26" aria-hidden="true">
      <polygon points="0,7 498,7 482,26 0,26" fill="var(--brand-grey)"/>
      <polygon points="516,0 748,0 748,26 488,26" fill="var(--brand-green)"/>
    </svg>
  </main>
</body>
</html>
```